Oil & Gas Consultants need a advertisement

We are advertising in some brochures and need a eye catching advertisement. The ads will be different sizes (some business card sized) and up to a full page ad. We want it clear, crisp and catches the eyes of our viewers. I need the ad to work with different sizes of advertising. We are oil and gas consultants who build gas facilities. We like the dark colors with our logo and want it to pop. Our website is www.tundralinefuel.com for more info on our company.

Target Market(s)

Oil & Gas Companies

Industry/Entity Type

Oil And Gas

Font styles to use
Serif
Sans Serif

Colors

Designer to choose colors to be used in the design.

Requirements
Must have
• our logo, our information how to contact us, what we do

```html
<!DOCTYPE html>
<html lang="en">
<head>
<meta charset="utf-8">
<title>Tundraline Fuel Services Inc — Oil &amp; Gas Services</title>
<link href="https://fonts.googleapis.com/css2?family=Montserrat:wght@500;600;700;800&display=swap" rel="stylesheet">
<style>
  :root {
    --ink-deep: #0d0d0d;
    --ink-mid: #2e2e2e;
    --ink-soft: #5a5a5a;
    --white: #ffffff;
    --text-light: #ececec;
    --gold: #c4920e;
    --frame: #bdbdbd;
  }
  * { margin: 0; padding: 0; box-sizing: border-box; }
  html, body { width: 1200px; height: 674px; overflow: hidden; background: var(--ink-deep); }
  body { font-family: "Montserrat", Arial, sans-serif; color: var(--white); }

  .ad { position: relative; width: 1200px; height: 674px; overflow: hidden; }

  .scene-photo {
    position: absolute; inset: 0;
    background:
      radial-gradient(ellipse at 30% 35%, #6e6e6e 0%, rgba(70,70,70,0.6) 35%, rgba(20,20,20,0) 70%),
      linear-gradient(180deg, #4d4d4d 0%, #3a3a3a 45%, #1e1e1e 75%, #0b0b0b 100%);
  }
  .footer-shade {
    position: absolute; left: 0; right: 0; bottom: 0; height: 150px;
    background: linear-gradient(180deg, rgba(0,0,0,0) 0%, rgba(0,0,0,0.75) 55%, #050505 100%);
  }

  .brand {
    position: absolute; left: 600px; top: 22px; width: 400px;
    display: flex; flex-direction: column; align-items: center;
  }
  .brand-mark { width: 92px; height: 92px; border-radius: 50%; background: #e3e3e3; }
  .brand-name {
    margin-top: 16px; text-align: center;
    font-weight: 600; font-size: 27px; line-height: 1.15; letter-spacing: 0.5px;
    color: var(--text-light);
  }

  .intro {
    position: absolute; left: 622px; top: 212px; width: 410px;
    font-size: 12.6px; font-weight: 500; line-height: 21px; color: var(--text-light);
  }

  .services {
    position: absolute; left: 615px; top: 346px; width: 408px; height: 205px;
    border: 1.5px solid var(--frame); border-radius: 6px;
    list-style: none; padding: 18px 0 0 16px;
  }
  .services li {
    display: flex; align-items: center; height: 35px;
    font-size: 15.2px; font-weight: 600; color: var(--white);
  }
  .services li .tick { width: 16px; height: 16px; margin-right: 8px; flex: none; }
  .services li .tick.second { margin-left: 14px; }

  .headline {
    position: absolute; left: 40px; top: 362px;
    font-weight: 700; text-transform: uppercase;
    font-size: 37px; line-height: 55px; letter-spacing: 0.3px;
  }
  .tagline {
    position: absolute; left: 38px; top: 470px;
    font-weight: 700; font-size: 55px; line-height: 70px;
  }
  .tagline .accent { color: var(--gold); }

  .contact {
    position: absolute; left: 46px; top: 610px; width: 1120px;
    display: flex; align-items: center; gap: 14px;
    font-size: 17.5px; font-weight: 600; color: var(--white); white-space: nowrap;
  }
  .contact .dot { width: 6px; height: 6px; border-radius: 50%; background: var(--white); }
</style>
</head>
<body>
  <main class="ad">
    <div class="scene-photo" role="img" aria-label="Monochrome photo of an engineer in a hard hat looking over a gas processing plant at dusk"></div>
    <div class="footer-shade"></div>

    <header class="brand">
      <div class="brand-mark"></div>
      <p class="brand-name">TUNDRALINE FUEL<br>SERVICES INC</p>
    </header>

    <p class="intro">Tundraline is a company based on experience and youth with a structured succession plan. With strong leadership and a variety of skill sets, we ensure the project will be completed in the most aggressive and efficient manner, all while holding safety with utmost regard.</p>

    <ul class="services">
      <li><svg class="tick" viewBox="0 0 16 16"><path d="M1.5 8.5 L6 13 L14.5 2.5" fill="none" stroke="#fff" stroke-width="2.6" stroke-linecap="round" stroke-linejoin="round"/></svg>Project Management</li>
      <li><svg class="tick" viewBox="0 0 16 16"><path d="M1.5 8.5 L6 13 L14.5 2.5" fill="none" stroke="#fff" stroke-width="2.6" stroke-linecap="round" stroke-linejoin="round"/></svg>Construction Management</li>
      <li><svg class="tick" viewBox="0 0 16 16"><path d="M1.5 8.5 L6 13 L14.5 2.5" fill="none" stroke="#fff" stroke-width="2.6" stroke-linecap="round" stroke-linejoin="round"/></svg>Facility Construction Inspection</li>
      <li><svg class="tick" viewBox="0 0 16 16"><path d="M1.5 8.5 L6 13 L14.5 2.5" fill="none" stroke="#fff" stroke-width="2.6" stroke-linecap="round" stroke-linejoin="round"/></svg>Pipeline Construction</li>
      <li><svg class="tick" viewBox="0 0 16 16"><path d="M1.5 8.5 L6 13 L14.5 2.5" fill="none" stroke="#fff" stroke-width="2.6" stroke-linecap="round" stroke-linejoin="round"/></svg>Inspection Expediting<svg class="tick second" viewBox="0 0 16 16"><path d="M1.5 8.5 L6 13 L14.5 2.5" fill="none" stroke="#fff" stroke-width="2.6" stroke-linecap="round" stroke-linejoin="round"/></svg>Cost Control</li>
    </ul>

    <h1 class="headline">The Pioneer<br>Consultant Leader in</h1>
    <p class="tagline"><span class="accent">Oil &amp; Gas</span> Services</p>

    <footer class="contact">
      <span>14 Ridgeway Park Drive, Calgary, Canada</span>
      <span class="dot"></span>
      <span>Phone: (403) 555-0147</span>
      <span class="dot"></span>
      <span>Email: info@tundralinefuel.com</span>
    </footer>
  </main>
</body>
</html>
```